Gobal construction supply company needs new business card design

I need a business card design for my global supply company using an existing logo. i will be looking to print these on rounded corner cards with the black background version of my logo on the back. on the front white background, my logo again and my simple details.

```html
<!DOCTYPE html>
<html lang="en">
<head>
<meta charset="utf-8">
<title>Meridian Build Supply – Business Card</title>
<link rel="stylesheet" href="https://fonts.googleapis.com/css2?family=Montserrat:wght@600;700&family=Open+Sans:wght@400;600&display=swap">
<style>
  :root {
    --page-bg: #e9e7e4;
    --card-black: #1e1e1e;
    --brand-red: #d40000;
    --text-light: #f2f2f2;
    --seal-white: #f6f6f6;
    --seal-shade: #dcdcdc;
    --ink-dark: #151515;
  }
  * { margin: 0; padding: 0; box-sizing: border-box; }
  html, body {
    width: 1200px; height: 900px; overflow: hidden;
    background: var(--page-bg);
  }
  .canvas { position: relative; width: 1200px; height: 900px; }

  .business-card {
    position: absolute; left: 209px; top: 210px;
    width: 782px; height: 480px;
    background: var(--card-black);
    overflow: hidden;
    box-shadow: 0 14px 40px rgba(0,0,0,0.18);
  }
  .red-band {
    position: absolute; top: 0; right: 0;
    width: 242px; height: 100%;
    background: var(--brand-red);
  }

  .identity { position: absolute; left: 48px; top: 62px; }
  .identity .person-name {
    font-family: "Montserrat", sans-serif; font-weight: 700;
    font-size: 26px; letter-spacing: 0.3px;
    color: var(--brand-red); line-height: 1.1;
  }
  .identity .person-role {
    font-family: "Open Sans", sans-serif; font-weight: 400;
    font-size: 21px; color: var(--text-light); margin-top: 2px;
  }

  .contact-list {
    position: absolute; left: 48px; top: 300px;
    list-style: none;
    font-family: "Open Sans", sans-serif; font-size: 21.5px;
    color: var(--text-light);
  }
  .contact-list li { display: flex; align-items: center; height: 29px; }
  .contact-list svg { width: 16px; height: 16px; margin-right: 12px; fill: var(--brand-red); flex: none; }

  .brand-seal {
    position: absolute; left: 316px; top: 24px;
    width: 440px; height: 440px; border-radius: 50%;
    background: radial-gradient(circle at 45% 40%, var(--seal-white) 0%, #eeeeee 60%, var(--seal-shade) 100%);
    display: flex; flex-direction: column; align-items: center; justify-content: center;
    gap: 18px;
  }
  .brand-seal .brand-dot {
    width: 34px; height: 34px; border-radius: 50%;
    background: var(--brand-red);
  }
  .brand-seal .brand-name {
    font-family: "Montserrat", sans-serif; font-weight: 700;
    font-size: 31px; line-height: 1.25; text-align: center;
    letter-spacing: 0.5px; color: var(--ink-dark);
  }
</style>
</head>
<body>
<main class="canvas">
  <section class="business-card">
    <div class="red-band"></div>

    <div class="identity">
      <p class="person-name">DANIEL HARTLEY</p>
      <p class="person-role">Managing Director</p>
    </div>

    <ul class="contact-list">
      <li>
        <svg viewBox="0 0 16 16" aria-hidden="true"><path d="M2 5c0-2 2-3 6-3s6 1 6 3v1.5h-3.5V5h-5v1.5H2z M3 8h10l1 6H2z M8 9.5a2 2 0 1 0 0 4 2 2 0 0 0 0-4z"/></svg>
        061-482 317 905
      </li>
      <li>
        <svg viewBox="0 0 16 16" aria-hidden="true"><path d="M4.5 1h7a1 1 0 0 1 1 1v12a1 1 0 0 1-1 1h-7a1 1 0 0 1-1-1V2a1 1 0 0 1 1-1zm1 2v8.5h5V3zm2.5 9.5a1 1 0 1 0 0 2 1 1 0 0 0 0-2z"/></svg>
        061-482 317 906
      </li>
      <li>
        <svg viewBox="0 0 16 16" aria-hidden="true"><path d="M1.5 3.5h13v9h-13z M1.5 3.5 8 9l6.5-5.5" stroke="#1e1e1e" stroke-width="1"/></svg>
        hello@meridianbuild.com
      </li>
      <li>
        <svg viewBox="0 0 16 16" aria-hidden="true"><circle cx="8" cy="8" r="7"/><path d="M5 4c2 0 2 2 4 2s0 3-2 3-1 3-3 2S3 4 5 4zm5 5c1.5 0 2 1 1 3s-2 0-2-1 0-2 1-2z" fill="#1e1e1e"/></svg>
        www.meridianbuild.com
      </li>
    </ul>

    <div class="brand-seal">
      <span class="brand-dot"></span>
      <p class="brand-name">MERIDIAN BUILD<br>SUPPLY</p>
    </div>
  </section>
</main>
</body>
</html>
```